Web design for construction/ handyman company. We are a new company and trying to brand ourselves.

We have a logo with a character already in place and want a user friendly and simple site. I'm attaching our logo designs with our Crocodile character to get an idea of our logo. We want people to remember us and our site. The name we chose was so we could use a logo with a character. Our name is Pelican Builders LLC.

Target Market(s)

New clients

Industry/Entity Type

Contractor

Coding

Coded - Design and coding required

Number of Pages Required

4 page

Font styles to use
Sans Serif

Requirements
Must have
• About Us Page, What we do (not sure what to call this), Contact Us, Home Page. Would like the same colors as on our business card designs to be used on the website.
Nice to have
• We eventually want a project page to add photos of projects but thats not necessary now. Would be nice to use the crocodile theme, hammer or something similar somehow in the page names or clicks.

```html
<!DOCTYPE html>
<html lang="en">
<head>
<meta charset="utf-8">
<title>Pelican Builders LLC</title>
<link rel="stylesheet" href="https://fonts.googleapis.com/css2?family=Open+Sans:wght@400;600;700;800&display=swap">
<style>
:root{
  --blue:#1f5ca9;
  --blue-dark:#17427c;
  --navy:#163763;
  --green:#3c9a2f;
  --green-light:#5cb83e;
  --ink:#333;
  --muted:#666;
  --card-line:#d3d8de;
  --white:#fff;
}
*{box-sizing:border-box;margin:0;padding:0}
html,body{width:702px;height:1200px;overflow:hidden}
body{position:relative;font-family:"Open Sans",Arial,sans-serif;color:var(--ink);background:var(--white)}
.abs{position:absolute}

/* header */
.contact-bar{left:300px;top:0;width:402px;height:26px;background:var(--blue);border-bottom-left-radius:14px;color:var(--white);font-size:11px;display:flex;align-items:center;gap:34px;padding-left:22px}
.contact-bar span{display:flex;align-items:center;gap:6px}
.brand{left:14px;top:14px;display:flex;align-items:center;gap:8px}
.brand-mark{width:26px;height:26px;background:var(--green);border-radius:50%}
.brand-name{font-size:17px;font-weight:800;color:var(--blue);line-height:1.05;width:130px}
.nav{left:278px;top:36px;display:flex;gap:6px}
.nav a{display:block;padding:8px 14px;font-size:11px;font-weight:600;color:var(--blue);text-decoration:none;border-radius:3px}
.nav a.active{background:var(--green);color:var(--white)}

/* hero */
.hero{left:0;top:92px;width:702px;height:296px;background:linear-gradient(180deg,#d9d4cc 0%,#bfb7aa 45%,#8b7c66 100%)}
.hero-arrow{top:188px;width:36px;height:48px;background:var(--blue);color:var(--white);font-size:26px;font-weight:700;display:flex;align-items:center;justify-content:center}
.hero-arrow.prev{left:0}
.hero-arrow.next{right:0}

/* about */
.mascot{left:26px;top:396px;width:150px;height:222px;background:linear-gradient(160deg,#6fb84f,#3d7f2e 60%,#2a5ea0);border-radius:40px 40px 12px 12px}
.about{left:272px;top:412px;width:412px}
.section-title{font-size:25px;font-weight:700;color:var(--blue);line-height:1.2}
.section-title em{font-style:normal;color:var(--green)}
.about p{margin-top:10px;font-size:10.5px;line-height:1.55;color:var(--muted)}
.btn{display:inline-block;background:var(--blue);color:var(--white);font-size:11px;font-weight:600;padding:7px 20px;border-radius:3px 14px 3px 14px}
.btn.dark{background:var(--navy);border-radius:3px}
.about .btn{margin-top:14px}

/* services */
.services{left:0;top:620px;width:702px;height:260px;background:linear-gradient(180deg,#cfd6cc,#b8c4bd 60%,#aab7b2)}
.services-title{left:0;top:640px;width:702px;text-align:center;font-size:25px;font-weight:700;line-height:1.2;color:var(--green)}
.services-title span{color:var(--blue)}
.card{top:692px;width:176px;height:176px;background:var(--white);border:1px solid var(--card-line);border-radius:6px;text-align:center;padding-top:70px}
.card-icon{position:absolute;left:61px;top:10px;width:52px;height:52px;border-radius:50%;background:var(--green);display:flex;align-items:center;justify-content:center}
.card h3{font-size:15px;font-weight:600;color:var(--blue)}
.card p{font-size:10px;line-height:1.4;color:var(--muted);padding:4px 14px 8px;height:46px}
.card-1{left:47px}.card-2{left:264px}.card-3{left:480px}

/* blog */
.blog{left:42px;top:904px;width:270px}
.blog .section-title{font-size:22px}
.post{display:flex;gap:8px;margin-top:10px}
.post-date{width:36px;height:38px;background:var(--green);color:var(--white);text-align:center;font-size:15px;font-weight:700;line-height:1.1;padding-top:3px;flex:none}
.post-date small{display:block;font-size:8px;font-weight:400}
.post p{font-size:9.5px;line-height:1.4;color:var(--muted)}
.post b{display:block;font-size:9px;color:var(--blue);margin-top:1px}

/* quote */
.quote{left:340px;top:904px;width:330px}
.quote .section-title{font-size:22px}
.quote-form{position:relative;margin-top:6px;height:200px}
.field{position:absolute;height:26px;border:1px solid #a9b6c6;border-radius:13px;font-size:9.5px;color:var(--muted);padding:6px 12px}
.submit{position:absolute;left:122px;top:170px;width:86px;height:24px;background:var(--blue);color:var(--white);font-size:10px;text-align:center;line-height:24px;border-radius:12px}

/* footer */
.footer{left:0;top:1148px;width:702px;height:52px;background:var(--navy);color:#c9d3e2;font-size:10px;display:flex;align-items:center;justify-content:space-between;padding:0 48px}
.footer em{font-style:normal;color:var(--green-light)}
.social{display:flex;gap:22px}
.social i{display:block;width:12px;height:12px;border-radius:50%;background:var(--green-light)}
</style>
</head>
<body>

<header>
  <div class="abs contact-bar">
    <span><svg width="12" height="9" viewBox="0 0 12 9"><rect x=".5" y=".5" width="11" height="8" fill="none" stroke="#fff"/><path d="M.5 .5 6 5l5.5-4.5" fill="none" stroke="#fff"/></svg>info@pelicanbuilders.example</span>
    <span><svg width="11" height="11" viewBox="0 0 11 11"><path d="M2 1l2 2-1 1.5c.7 1.4 1.9 2.6 3.3 3.3L7.8 6.8l2 2L8.6 10C4.5 9.6 1.4 6.5 1 2.4z" fill="#fff"/></svg>(555) 014-2290</span>
  </div>
  <div class="abs brand">
    <div class="brand-mark"></div>
    <div class="brand-name">Pelican Builders LLC</div>
  </div>
  <nav class="abs nav">
    <a class="active" href="#">HOME</a>
    <a href="#">ABOUT US</a>
    <a href="#">SERVICES</a>
    <a href="#">PROJECTS</a>
    <a href="#">CONTACT US</a>
  </nav>
</header>

<section class="abs hero" role="img" aria-label="Photo of a renovated white kitchen with an island and bar stools"></section>
<div class="abs hero-arrow prev">&laquo;</div>
<div class="abs hero-arrow next">&raquo;</div>

<section>
  <div class="abs mascot" role="img" aria-label="Company mascot character holding a hammer"></div>
  <div class="abs about">
    <h2 class="section-title">About <em>PELICAN BUILDERS LLC</em></h2>
    <p>Pelican Builders LLC is a family owned and operated business of Dale and Family. Dale Morrow serving the Central Texas areas. Dale Morrow started as a professional precision machinist, serving his own machine shop through the 70's, 80's and 90's. Back in 1996, Dale started in the remodeling business for investment properties in the Houston metro area as well as Central Texas. After almost 20 years of being focused on just investors, Dale decided to expand his services to the general public as well.</p>
    <span class="btn">Read More</span>
  </div>
</section>

<section>
  <div class="abs services" role="img" aria-label="Faded photo of a building exterior"></div>
  <h2 class="abs services-title">PELICAN BUILDERS LLC <span>Services</span></h2>

  <div class="abs card card-1">
    <div class="card-icon"><svg width="26" height="26" viewBox="0 0 26 26"><path d="M5 21 16 10" stroke="#fff" stroke-width="3" stroke-linecap="round"/><circle cx="18" cy="8" r="4.5" fill="none" stroke="#fff" stroke-width="2.5"/><path d="M5 5l16 16" stroke="#fff" stroke-width="2.5" stroke-linecap="round"/></svg></div>
    <h3>Handyman Services</h3>
    <p>Including decks, patios, fences, doors and more.</p>
    <span class="btn dark">Read More</span>
  </div>
  <div class="abs card card-2">
    <div class="card-icon"><svg width="26" height="26" viewBox="0 0 26 26"><rect x="13" y="3" width="9" height="9" rx="1.5" transform="rotate(45 17.5 7.5)" fill="#fff"/><path d="M14 12 6 20" stroke="#fff" stroke-width="3" stroke-linecap="round"/></svg></div>
    <h3>Painting</h3>
    <p>Interior and exterior including walls, trim, doors, cabinets, decks and more.</p>
    <span class="btn dark">Read More</span>
  </div>
  <div class="abs card card-3">
    <div class="card-icon"><svg width="26" height="26" viewBox="0 0 26 26"><path d="M3 18 13 13l10 5-10 5z" fill="#fff"/><path d="M3 12 13 7l10 5-10 5z" fill="none" stroke="#fff" stroke-width="2"/></svg></div>
    <h3>Flooring</h3>
    <p>New installation and repairs of tile, carpet, wood, concrete and laminate flooring.</p>
    <span class="btn dark">Read More</span>
  </div>
</section>

<section class="abs blog">
  <h2 class="section-title">Latest <em>Blog</em></h2>
  <div class="post"><div class="post-date">25<small>May</small></div><p>Lorem Ipsum is simply dummy text of the printing and typesetting industry.<b>READ MORE</b></p></div>
  <div class="post"><div class="post-date">20<small>May</small></div><p>Lorem Ipsum is simply dummy text of the printing and typesetting industry.<b>READ MORE</b></p></div>
  <div class="post"><div class="post-date">20<small>May</small></div><p>Lorem Ipsum is simply dummy text of the printing and typesetting industry.<b>READ MORE</b></p></div>
</section>

<section class="abs quote">
  <h2 class="section-title">Get&nbsp; Quotes to <em>Free Estimates</em></h2>
  <div class="quote-form">
    <div class="field" style="left:0;top:0;width:156px">Name</div>
    <div class="field" style="left:172px;top:0;width:156px">Contact No.</div>
    <div class="field" style="left:0;top:38px;width:328px">Email Id</div>
    <div class="field" style="left:0;top:76px;width:328px;height:84px;border-radius:14px">Message</div>
    <div class="submit">Submit</div>
  </div>
</section>

<footer class="abs footer">
  <span>&copy; <em>Pelican Builders LLC</em> - 2015. All Rights Reserved</span>
  <div class="social"><i></i><i></i><i></i></div>
</footer>

</body>
</html>
```